Dufresne Roofing

Want a professional looking business card

Industry/Entity Type

Business

Contact Information for Business Card

Marc Dufresne ( Owner) marc@dufresneroofing-example.com, www.dufresneroofing-example.com, Adress: 4217 County road 42 Wendover,ON K0A3M1

```html
<!DOCTYPE html>
<html lang="en">
<head>
<meta charset="utf-8">
<title>Dufresne Roofing – Business Card</title>
<link rel="stylesheet" href="https://fonts.googleapis.com/css2?family=Open+Sans:wght@400;600;700;800&display=swap">
<style>
  :root {
    --bg: #e6e8eb;
    --blue-light: #2b74db;
    --blue-dark: #1a448f;
    --blue-brand: #1f4e9c;
    --grey-text: #6b6f75;
    --grey-band: #9a9ea4;
    --line: #c9ccd0;
    --paper: #fafafa;
    --white: #ffffff;
  }
  * { box-sizing: border-box; margin: 0; padding: 0; }
  html, body { width: 1200px; height: 900px; overflow: hidden; }
  body {
    background: var(--bg);
    font-family: "Open Sans", Arial, sans-serif;
    position: relative;
  }
  .card {
    position: absolute;
    left: 285px;
    width: 630px;
    height: 360px;
    border-radius: 4px;
    overflow: hidden;
    box-shadow: 0 6px 18px rgba(0,0,0,0.15);
  }
  .card--front {
    top: 60px;
    background: linear-gradient(35deg, var(--blue-light) 0%, var(--blue-dark) 75%);
  }
  .card--back {
    top: 480px;
    background: var(--paper);
  }
  .brand {
    display: flex;
    align-items: center;
    gap: 14px;
    font-weight: 800;
    text-transform: uppercase;
    letter-spacing: 1px;
    line-height: 1;
  }
  .brand__mark { display: block; width: 22px; height: 22px; }
  .card--front .brand {
    position: absolute; left: 0; right: 0; top: 130px;
    justify-content: center;
    color: var(--white);
    font-size: 40px;
  }
  .card--front .brand__mark { background: var(--white); }
  .front__web {
    position: absolute; left: 0; right: 0; bottom: 46px;
    text-align: center;
    color: var(--white);
    font-size: 14px;
    letter-spacing: 5px;
  }
  .card--back .brand {
    position: absolute; right: 30px; top: 62px;
    color: var(--blue-brand);
    font-size: 30px;
  }
  .card--back .brand__mark { background: var(--blue-brand); width: 18px; height: 18px; }
  .back__art { position: absolute; inset: 0; }
  .address {
    position: absolute; right: 30px; top: 166px;
    text-align: right;
    color: var(--grey-text);
    font-size: 14px;
    line-height: 1.5;
  }
  .back__web {
    position: absolute; right: 22px; top: 236px;
    color: var(--white);
    font-size: 13px;
    font-weight: 600;
    line-height: 20px;
    white-space: nowrap;
  }
  .person { position: absolute; left: 30px; top: 198px; }
  .person__name {
    color: var(--blue-brand);
    font-size: 21px;
    font-weight: 700;
    line-height: 28px;
    text-transform: uppercase;
  }
  .person__role {
    color: var(--grey-text);
    font-size: 14px;
    line-height: 20px;
    letter-spacing: 1px;
    margin-bottom: 6px;
  }
  .contact {
    list-style: none;
    color: var(--grey-text);
    font-size: 13px;
    line-height: 1.7;
  }
  .contact li { display: flex; align-items: center; gap: 8px; }
  .contact svg { width: 12px; height: 12px; fill: var(--blue-brand); }
</style>
</head>
<body>

<section class="card card--front">
  <div class="brand"><span class="brand__mark"></span>Dufresne Roofing</div>
  <p class="front__web">www.dufresneroofing-example.com</p>
</section>

<section class="card card--back">
  <svg class="back__art" viewBox="0 0 630 360" aria-hidden="true">
    <line x1="250" y1="142" x2="600" y2="142" stroke="var(--line)" stroke-width="1"/>
    <line x1="100" y1="237" x2="300" y2="237" stroke="var(--line)" stroke-width="1"/>
    <polygon points="328,262 358,230 630,230 630,262" fill="var(--blue-brand)"/>
    <polygon points="0,318 300,318 352,266 630,266 630,278 358,278 306,330 0,330" fill="var(--grey-band)"/>
    <rect x="0" y="338" width="630" height="22" fill="var(--blue-brand)"/>
  </svg>

  <div class="brand"><span class="brand__mark"></span>Dufresne Roofing</div>

  <p class="address">4217 County road 42<br>Wendover, ON K0A3M1</p>
  <p class="back__web">www.dufresneroofing-example.com</p>

  <div class="person">
    <h1 class="person__name">Marc Dufresne</h1>
    <p class="person__role">OWNER</p>
    <ul class="contact">
      <li>
        <svg viewBox="0 0 24 24"><path d="M6.6 10.8a15.1 15.1 0 0 0 6.6 6.6l2.2-2.2c.3-.3.7-.4 1-.2 1.1.4 2.3.6 3.6.6.6 0 1 .4 1 1V20c0 .6-.4 1-1 1A17 17 0 0 1 3 4c0-.6.4-1 1-1h3.5c.6 0 1 .4 1 1 0 1.3.2 2.5.6 3.6.1.3 0 .7-.2 1z"/></svg>
        613 555 0148
      </li>
      <li>
        <svg viewBox="0 0 24 24"><path d="M2 5h20v14H2z" fill="var(--blue-brand)"/><path d="M3 6l9 7 9-7" fill="none" stroke="#fff" stroke-width="1.5"/></svg>
        marc@dufresneroofing-example.com
      </li>
    </ul>
  </div>
</section>

</body>
</html>
```